Massage Center New Ad

You will be creating a 5 X 7" Massage Ad.
All the text content remains the same as example provided
however looking for a "COMPLETELY DIFFERENT" Look.
Feel free to use photo images, clip art images, Black & white, etc. Remember it should different than example.
Emphasis on the PROMO of a 30 minute massage for Only $15. Logo Attached.
Reason: Still looking for the piece that stands out....Thanks
Massage

```html
<!DOCTYPE html>
<html lang="en">
<head>
<meta charset="utf-8">
<title>Coral Bay Massage Centers – Grand Opening</title>
<link rel="stylesheet" href="https://fonts.googleapis.com/css2?family=Merienda:wght@600;700&family=Ubuntu:ital,wght@0,700;1,700&display=swap">
<style>
  :root {
    --backdrop: #3a0a0c;
    --sky-top: #f4f8fc;
    --sky-mid: #6aa9dc;
    --sky-deep: #5d9fd6;
    --title-blue: #2a8fd6;
    --title-blue-deep: #1c63b8;
    --promo-red: #d3202b;
    --ink: #1f1f22;
    --service-navy: #24308a;
    --band-white: #f3f6fa;
    --burst-light: #ffffff;
    --burst-shade: #c9ccd2;
    --sun-orange: #f6a21e;
  }
  * { margin: 0; padding: 0; box-sizing: border-box; }
  html, body { width: 900px; height: 1200px; overflow: hidden; }
  body { background: var(--backdrop); position: relative; font-family: "Ubuntu", sans-serif; }

  .flyer {
    position: absolute; left: 78px; top: 80px; width: 750px; height: 1050px;
    overflow: hidden;
    background: linear-gradient(180deg, var(--sky-top) 0%, #dfeaf5 10%, var(--sky-mid) 17%, var(--sky-deep) 55%, #9cc6e6 70%, #eef3f8 100%);
  }
  .header-wave { position: absolute; left: 0; top: 0; width: 750px; height: 200px; }
  .photo-area {
    position: absolute; left: 0; top: 540px; width: 750px; height: 460px;
    background: linear-gradient(180deg, rgba(93,159,214,0) 0%, #a8cde9 22%, #e3eef6 38%, #d9b79c 62%, #f1e6dc 82%, #ffffff 100%);
  }
  .footer-wave { position: absolute; left: 0; bottom: 0; width: 750px; height: 120px; }

  .grand-opening {
    position: absolute; left: 36px; top: 18px;
    font-family: "Merienda", cursive; font-weight: 700; font-size: 54px;
    color: var(--title-blue); transform: rotate(4deg); transform-origin: left top;
    text-shadow: 2px 2px 0 #fff, 3px 4px 4px rgba(0,0,0,.2);
  }
  .headline {
    position: absolute; left: 30px; top: 158px;
    font-weight: 700; font-size: 84px; color: var(--promo-red);
    text-shadow: 2px 2px 0 #fff, 4px 5px 6px rgba(0,0,0,.3);
  }
  .tagline {
    position: absolute; left: 28px; top: 252px;
    font-weight: 700; font-style: italic; font-size: 37px; color: var(--ink);
    text-shadow: 0 0 3px #fff, 2px 2px 0 #fff, 3px 4px 5px rgba(0,0,0,.35);
  }

  .promo { position: absolute; left: 17px; top: 372px; width: 392px; height: 270px; }
  .promo svg { position: absolute; inset: 0; width: 100%; height: 100%; }
  .promo-text {
    position: absolute; inset: 0; display: flex; flex-direction: column;
    align-items: center; justify-content: center; text-align: center;
  }
  .promo-line { font-weight: 700; font-size: 40px; line-height: 48px; color: var(--ink); text-shadow: 1px 2px 2px rgba(0,0,0,.25); }
  .promo-price { font-weight: 700; font-style: italic; font-size: 56px; line-height: 66px; color: var(--promo-red); text-shadow: 2px 3px 3px rgba(0,0,0,.3); }

  .services {
    position: absolute; right: 28px; top: 383px; list-style: none; text-align: right;
    font-family: "Merienda", cursive; font-weight: 600; font-size: 27px; line-height: 40px;
    color: var(--service-navy); text-shadow: 1px 1px 0 #fff, -1px -1px 0 #fff, 1px -1px 0 #fff, -1px 1px 0 #fff;
  }

  .brand {
    position: absolute; right: 26px; top: 868px; display: flex; align-items: center; gap: 14px;
  }
  .brand-mark { width: 60px; height: 60px; border-radius: 50%; background: var(--sun-orange); }
  .brand-name {
    font-weight: 700; font-size: 38px; line-height: 40px; color: var(--title-blue-deep);
  }

  .contact {
    position: absolute; left: 20px; top: 1018px; display: flex; gap: 38px;
    font-family: Arial, Helvetica, sans-serif; font-size: 16px; color: var(--ink);
  }
</style>
</head>
<body>
  <main class="flyer">
    <svg class="header-wave" viewBox="0 0 750 200" aria-hidden="true">
      <path d="M0 150 C 160 95, 330 95, 470 145 S 680 180, 750 110 L750 0 L0 0 Z" fill="rgba(255,255,255,.35)"/>
      <path d="M0 150 C 160 95, 330 95, 470 145 S 680 180, 750 110" fill="none" stroke="#ffffff" stroke-width="5"/>
    </svg>

    <div class="photo-area" role="img" aria-label="Photo of a woman receiving a back massage on a table beside the sea, with a candle bowl in front"></div>

    <svg class="footer-wave" viewBox="0 0 750 120" aria-hidden="true">
      <path d="M0 70 C 180 20, 420 20, 560 50 S 710 60, 750 30 L750 120 L0 120 Z" fill="var(--band-white)"/>
      <path d="M0 70 C 180 20, 420 20, 560 50 S 710 60, 750 30" fill="none" stroke="#7fb2de" stroke-width="3"/>
    </svg>

    <h2 class="grand-opening">Grand Opening</h2>
    <h1 class="headline">Massage</h1>
    <p class="tagline">Licensed Professional stress relief</p>

    <div class="promo">
      <svg viewBox="0 0 100 100" preserveAspectRatio="none" aria-hidden="true">
        <defs>
          <radialGradient id="burstFill" cx="50%" cy="45%" r="60%">
            <stop offset="0%" stop-color="var(--burst-light)"/>
            <stop offset="70%" stop-color="#eceef1"/>
            <stop offset="100%" stop-color="var(--burst-shade)"/>
          </radialGradient>
        </defs>
        <polygon fill="url(#burstFill)" stroke="#b5b9c0" stroke-width=".4" points="100,50 91.6,55.5 98.3,62.9 88.8,66.1 93.3,75 83.3,75.6 85.4,85.4 75.6,83.3 75,93.3 66.1,88.8 62.9,98.3 55.5,91.6 50,100 44.5,91.6 37.1,98.3 33.9,88.8 25,93.3 24.4,83.3 14.6,85.4 16.7,75.6 6.7,75 11.2,66.1 1.7,62.9 8.4,55.5 0,50 8.4,44.5 1.7,37.1 11.2,33.9 6.7,25 16.7,24.4 14.6,14.6 24.4,16.7 25,6.7 33.9,11.2 37.1,1.7 44.5,8.4 50,0 55.5,8.4 62.9,1.7 66.1,11.2 75,6.7 75.6,16.7 85.4,14.6 83.3,24.4 93.3,25 88.8,33.9 98.3,37.1 91.6,44.5"/>
      </svg>
      <div class="promo-text">
        <span class="promo-line">A 30 minute</span>
        <span class="promo-line">massage for</span>
        <span class="promo-price">Only $15</span>
      </div>
    </div>

    <ul class="services">
      <li>Reflexology</li>
      <li>Sports Massage</li>
      <li>Trigger Point Therapy</li>
      <li>Relaxation Massage</li>
      <li>Deep Tissue</li>
      <li>Injury Massage</li>
      <li>Swedish</li>
    </ul>

    <div class="brand">
      <span class="brand-mark" aria-hidden="true"></span>
      <span class="brand-name">Coral Bay<br>Massage Centers</span>
    </div>

    <footer class="contact">
      <span>Ph: +91 555 010 234</span>
      <span>Add: 118, Harbor Lane. wb. US</span>
    </footer>
  </main>
</body>
</html>
```